Corvane Supplies Business Card

Professional business card that stand out to our potential customers. Front and back with clean modern design

Industry/Entity Type

Oil and gas

Contact Information for Business Card

Name, address, website , office phone and cell number

Requirements
Must have
• Editable files for each employee

```html
<!DOCTYPE html>
<html lang="en">
<head>
<meta charset="utf-8">
<title>Corvane Supplies Business Card</title>
<link href="https://fonts.googleapis.com/css2?family=Montserrat:wght@400;500;700;800&display=swap" rel="stylesheet">
<style>
  :root {
    --stage: #2e2e30;
    --card: #ffffff;
    --brand-red: #e4202a;
    --brand-cyan: #1aadd0;
    --ink: #2a2a2a;
  }
  * { margin: 0; padding: 0; box-sizing: border-box; }
  html, body { width: 1200px; height: 875px; overflow: hidden; }
  body {
    background: var(--stage);
    font-family: "Montserrat", Arial, sans-serif;
    display: flex;
    flex-direction: column;
    align-items: center;
    justify-content: center;
    gap: 34px;
  }
  .card {
    width: 700px;
    height: 400px;
    background: var(--card);
    border-radius: 26px;
    position: relative;
    box-shadow: 0 10px 30px rgba(0,0,0,.35);
  }
  .wordmark {
    display: flex;
    align-items: center;
    gap: 14px;
    color: var(--brand-red);
    font-weight: 800;
    text-transform: uppercase;
    letter-spacing: 1px;
  }
  .wordmark .mark-square {
    background: var(--brand-red);
    flex: none;
  }
  /* Front */
  .card-front {
    display: flex;
    align-items: center;
    justify-content: center;
  }
  .card-front .wordmark { font-size: 44px; }
  .card-front .mark-square { width: 42px; height: 42px; }
  /* Back */
  .card-back {
    display: flex;
    align-items: center;
    padding: 0 46px 0 56px;
  }
  .card-back .wordmark { font-size: 25px; width: 300px; gap: 10px; }
  .card-back .mark-square { width: 24px; height: 24px; }
  .divider {
    width: 2px;
    height: 250px;
    background: var(--brand-red);
    margin: 0 26px 0 14px;
  }
  .contact { color: var(--ink); }
  .contact .person-name {
    color: var(--brand-red);
    font-weight: 700;
    font-size: 27px;
    line-height: 1.1;
  }
  .contact .person-title {
    font-size: 16px;
    margin: 2px 0 16px;
  }
  .contact ul { list-style: none; }
  .contact li {
    display: flex;
    align-items: center;
    gap: 10px;
    font-size: 15.5px;
    line-height: 1.65;
  }
  .contact li svg { width: 15px; height: 15px; flex: none; fill: var(--brand-cyan); }
  .contact address {
    font-style: normal;
    font-size: 15.5px;
    line-height: 1.35;
    margin-top: 12px;
  }
</style>
</head>
<body>
  <section class="card card-front" aria-label="Card front">
    <div class="wordmark"><span class="mark-square"></span><span>Corvane Supplies</span></div>
  </section>

  <section class="card card-back" aria-label="Card back">
    <div class="wordmark"><span class="mark-square"></span><span>Corvane Supplies</span></div>
    <div class="divider"></div>
    <div class="contact">
      <div class="person-name">Daren Holloway</div>
      <div class="person-title">President</div>
      <ul>
        <li>
          <svg viewBox="0 0 24 24" aria-hidden="true"><path d="M3 8c0-3 4-5 9-5s9 2 9 5v2h-5V8H8v2H3zM6 11h12l2 9H4zm6 2.5a3 3 0 1 0 0 6 3 3 0 0 0 0-6z"/></svg>
          +1.555.210.0400 x123
        </li>
        <li>
          <svg viewBox="0 0 24 24" aria-hidden="true"><path d="M7 1h10a2 2 0 0 1 2 2v18a2 2 0 0 1-2 2H7a2 2 0 0 1-2-2V3a2 2 0 0 1 2-2zm0 3v14h10V4zm5 15.5a1.2 1.2 0 1 0 0 2.4 1.2 1.2 0 0 0 0-2.4z"/></svg>
          +1.555.123.456
        </li>
        <li>
          <svg viewBox="0 0 24 24" aria-hidden="true"><path d="M2 5h20v14H2zm2 2v.5l8 5.5 8-5.5V7zm0 3v7h16v-7l-8 5.5z"/></svg>
          info@corvanesupplies.com
        </li>
        <li>
          <svg viewBox="0 0 24 24" aria-hidden="true"><path d="M12 2a10 10 0 1 0 0 20 10 10 0 0 0 0-20zm6.9 9h-3a15 15 0 0 0-1.3-6 8 8 0 0 1 4.3 6zM12 4.1c.9 1.3 1.7 3.8 1.9 6.9h-3.8c.2-3.1 1-5.6 1.9-6.9zM9.4 5a15 15 0 0 0-1.3 6h-3a8 8 0 0 1 4.3-6zm-4.3 8h3a15 15 0 0 0 1.3 6 8 8 0 0 1-4.3-6zm6.9 6.9c-.9-1.3-1.7-3.8-1.9-6.9h3.8c-.2 3.1-1 5.6-1.9 6.9zm2.6-.9a15 15 0 0 0 1.3-6h3a8 8 0 0 1-4.3 6z"/></svg>
          www.corvanesupplies.com
        </li>
      </ul>
      <address>48 Ridgeline Plaza<br>Halden, TX 79701 USA</address>
    </div>
  </section>
</body>
</html>
```